Re-design of veterinary clinic website *

For a future relaunch of our webpage, we would like to find a fresh design that still incorporates the spirit of our current one which can be found at http://dr-wenzlaff.de
We are a small business that appeals to locals but are known in a wide area for specialist services.
According to analytics data, most people rarely read through the full website but are using it to inform themselves about opening hours, Telephone numbers and location. Still, the website needs to offer enough content to be ranked positively by the Quandle algorithm.
Our logo is not part of the re-design but needs to be included in your proposal as is. It can be used a source of inspiration, just as the current design. Keep in mind, that the design will be used as the basis of a fluid webdesign for both mobile and desktop. Roughly 75% of our users are on mobile devices.
Target Market(s)
Locals
Industry/Entity Type
Veterinary
Number of Pages Required
1 page
Look and feel
Each slider illustrates characteristics of the customer's brand and the style your logo design should communicate.

```html
<!DOCTYPE html>
<html lang="de">
<head>
<meta charset="utf-8">
<title>Tierarztpraxis Dr. Heinrich Wenzlaff</title>
<link href="https://fonts.googleapis.com/css2?family=Mulish:wght@400;600;700&family=Open+Sans:wght@400;600&display=swap" rel="stylesheet">
<style>
  :root {
    --navy: #2d3f8a;
    --sky: #3ea9e0;
    --paw: #8ecbea;
    --panel-light: #41b1e3;
    --panel-mid: #0784d0;
    --panel-dark: #3157a6;
    --heading-grey: #677789;
    --white: #ffffff;
  }
  * { margin: 0; padding: 0; box-sizing: border-box; }
  html, body { width: 1200px; height: 1000px; overflow: hidden; background: var(--white); }
  body { font-family: "Mulish", sans-serif; position: relative; }

  .paw { position: absolute; left: 50%; transform: translateX(-50%); }

  .welcome { position: absolute; top: 0; left: 0; width: 1200px; height: 265px; text-align: center; }
  .welcome .paw { top: 16px; }
  .welcome h1 { position: absolute; top: 76px; width: 100%; font-size: 28px; font-weight: 700; color: var(--navy); }
  .welcome p { position: absolute; top: 128px; width: 100%; font-size: 19px; line-height: 24px; color: var(--sky); }
  .welcome strong { font-weight: 700; }

  .info-band { position: absolute; top: 265px; left: 0; width: 1200px; height: 249px; display: flex; color: var(--white); }
  .info-panel { height: 100%; padding: 28px 28px 0; position: relative; }
  .info-panel.team { width: 399px; background: var(--panel-light); padding-left: 25px; }
  .info-panel.booking { width: 401px; background: var(--panel-mid); }
  .info-panel.hours { width: 400px; background: var(--panel-dark); font-family: "Open Sans", sans-serif; }
  .info-panel h2 { font-size: 22px; font-weight: 400; margin-bottom: 16px; }
  .info-panel.hours h2 { font-weight: 600; font-size: 21px; }
  .info-panel p { font-size: 14.5px; line-height: 19.5px; }
  .info-panel.booking p { line-height: 24.5px; margin-top: -4px; }
  .outline-btn { position: absolute; top: 176px; left: 28px; height: 46px; border: 1px solid var(--white); display: flex; align-items: center; gap: 8px; padding: 0 18px; font-size: 14px; font-weight: 600; text-transform: uppercase; color: var(--white); }
  .info-panel.team .outline-btn { left: 27px; width: 141px; }
  .info-panel.booking .outline-btn { width: 141px; padding-left: 13px; font-weight: 400; }

  .slider-controls { position: absolute; top: 22px; right: 28px; display: flex; }
  .slider-controls span { width: 34px; height: 36px; border: 1px solid rgba(255,255,255,0.3); display: flex; align-items: center; justify-content: center; }
  .slider-controls span + span { border-left: none; }

  .hours-list { list-style: none; margin-top: 18px; }
  .hours-list li { display: flex; justify-content: space-between; height: 49px; align-items: center; border-bottom: 1px solid rgba(255,255,255,0.22); font-size: 14px; font-weight: 600; }
  .hours-list li:first-child { height: 40px; align-items: flex-start; padding-top: 7px; }

  .services { position: absolute; top: 514px; left: 0; width: 1200px; height: 486px; }
  .services .paw { top: 42px; }
  .services h2 { position: absolute; top: 90px; width: 100%; text-align: center; font-size: 35px; font-weight: 400; color: var(--heading-grey); }
  .service-card { position: absolute; top: 174px; width: 322px; height: 330px; background: var(--white); border-radius: 22px 22px 0 0; box-shadow: 0 0 8px rgba(0,0,0,0.22); overflow: hidden; }
  .service-card .photo { height: 284px; }
  .card-dogs { left: 74px; }
  .card-cats { left: 435px; }
  .card-small { left: 797px; }
  .card-dogs .photo { background: linear-gradient(160deg, #b0622a, #7c3f1c 55%, #c8a58a); }
  .card-cats .photo { background: linear-gradient(150deg, #5a2a18, #c3743c 45%, #e8e2dc 80%); }
  .card-small .photo { background: linear-gradient(160deg, #f2f2f2, #9b8574 50%, #f0d060 85%); }
</style>
</head>
<body>

<section class="welcome">
  <svg class="paw" width="42" height="38" viewBox="0 0 42 38" aria-hidden="true">
    <g fill="var(--paw)">
      <ellipse cx="8" cy="15" rx="4.5" ry="5.5"/>
      <ellipse cx="16" cy="7" rx="4.5" ry="6"/>
      <ellipse cx="26" cy="7" rx="4.5" ry="6"/>
      <ellipse cx="34" cy="15" rx="4.5" ry="5.5"/>
      <path d="M21 17c-6 0-12 8-12 13 0 4 4 5 7 4s3-2 5-2 2 1 5 2 7 0 7-4c0-5-6-13-12-13z"/>
    </g>
  </svg>
  <h1>Herzlich Willkommen!</h1>
  <p>Herzlich Willkommen auf der Homepage der Tierarztpraxis von <strong>Dr. Heinrich Wenzlaff</strong>.<br>
  Mein Team und ich haben hier Informationen rund um die Praxis und<br>
  Hinweise für Patientenbesitzer zusammengestellt.</p>
</section>

<section class="info-band">
  <div class="info-panel team">
    <h2>Meet Our Team</h2>
    <p>Das Praxisteam besteht aus einer<br>angestellten Tierärztin, einem angestellten<br>Tierarzt, mehreren tiermedizinischen<br>Fachangestellten und Auszubildenden sowie mir.</p>
    <a class="outline-btn">Read more
      <svg width="14" height="10" viewBox="0 0 14 10"><path d="M1 5h11M8 1l4 4-4 4" stroke="#fff" stroke-width="1.5" fill="none"/></svg></a>
  </div>
  <div class="info-panel booking">
    <h2>Book Appointment</h2>
    <p>We will review your request<br>and confirm your appointment<br>as soon as possible.</p>
    <a class="outline-btn">Book now
      <svg width="14" height="10" viewBox="0 0 14 10"><path d="M1 5h11M8 1l4 4-4 4" stroke="#fff" stroke-width="1.5" fill="none"/></svg></a>
  </div>
  <div class="info-panel hours">
    <h2>Opening Hours</h2>
    <div class="slider-controls">
      <span><svg width="8" height="10" viewBox="0 0 8 10"><path d="M6 1L2 5l4 4" stroke="#fff" stroke-width="1.4" fill="none"/></svg></span>
      <span><svg width="8" height="10" viewBox="0 0 8 10"><path d="M2 1l4 4-4 4" stroke="#fff" stroke-width="1.4" fill="none"/></svg></span>
    </div>
    <ul class="hours-list">
      <li><span>Monday - Thursday</span><span>8.00 - 17.00</span></li>
      <li><span>Friday</span><span>9.00 - 18.00</span></li>
      <li><span>Saturday</span><span>9.30 - 17.30</span></li>
    </ul>
  </div>
</section>

<section class="services">
  <svg class="paw" width="42" height="38" viewBox="0 0 42 38" aria-hidden="true">
    <g fill="var(--paw)">
      <ellipse cx="8" cy="15" rx="4.5" ry="5.5"/>
      <ellipse cx="16" cy="7" rx="4.5" ry="6"/>
      <ellipse cx="26" cy="7" rx="4.5" ry="6"/>
      <ellipse cx="34" cy="15" rx="4.5" ry="5.5"/>
      <path d="M21 17c-6 0-12 8-12 13 0 4 4 5 7 4s3-2 5-2 2 1 5 2 7 0 7-4c0-5-6-13-12-13z"/>
    </g>
  </svg>
  <h2>Unsere Dienstleistungen</h2>
  <article class="service-card card-dogs"><div class="photo" role="img" aria-label="Foto eines braunen Hundes, der den Kopf ablegt"></div></article>
  <article class="service-card card-cats"><div class="photo" role="img" aria-label="Foto einer rot-weißen Langhaarkatze"></div></article>
  <article class="service-card card-small"><div class="photo" role="img" aria-label="Foto eines Widderkaninchens mit einem Entenküken"></div></article>
</section>

</body>
</html>
```